Micropayment solution needs a Wordpress Design

We need a wordpress design for a new company based in London. Micropayment and mobile payment technologies. Varnel, Quorvath, Fembrisk payments.
We need a one page website design.

If you have any question, please don't hesitate to contact us.

Industry/Entity Type

It Company

Font styles to use
Other font styles liked:
• Maven Pro

Requirements
Must have
• We need a clean and user friendly interface.
Should not have
• we don't wanna to see rounded pages.

```html
<!DOCTYPE html>
<html lang="en">
<head>
<meta charset="utf-8">
<title>Micropayment Solutions</title>
<link rel="stylesheet" href="https://fonts.googleapis.com/css2?family=Maven+Pro:wght@400;500;700&display=swap">
<style>
:root{
  --ink:#2b2b2b;
  --muted:#555;
  --white:#fff;
  --red:#d4262c;
  --dark:#2a2a2a;
  --light:#f2f2f2;
  --purple:#2f2b63;
  --navy:#2f3d57;
  --teal:#24a384;
  --footer:#222;
  --line:#ddd;
}
*{margin:0;padding:0;box-sizing:border-box}
html,body{width:1200px;height:5014px;overflow:hidden}
body{font-family:"Maven Pro",Arial,sans-serif;color:var(--ink);background:var(--white);font-size:14px;line-height:1.6}
section,header,footer{position:relative;width:1200px;overflow:hidden}
.title{font-size:30px;font-weight:400;text-align:center}
.title b{font-weight:700}
.rule{width:64px;height:2px;background:var(--ink);margin:10px auto 26px}
.copy{width:1060px;margin:0 auto;text-align:center;font-size:13.5px;line-height:1.75;color:var(--muted)}
.btn{display:inline-block;padding:9px 34px;font-size:14px;border:2px solid var(--white);color:var(--white);text-decoration:none}
.btn-solid{background:var(--white);color:var(--ink)}
.btn-dark{background:var(--ink);color:var(--white);border-color:var(--ink)}
.tiles{display:flex;justify-content:center;gap:22px}
.tile{width:150px;height:96px;border:1px solid var(--line);background:var(--white);display:flex;align-items:center;justify-content:center;gap:8px;font-size:17px;font-weight:500;color:var(--ink)}
.tile .dot{width:18px;height:18px;border-radius:50%;background:currentColor}
.dots{display:flex;justify-content:center;gap:8px}
.dots i{width:9px;height:9px;border-radius:50%;background:#bbb}
.dots i.on{background:var(--ink)}

/* hero */
.hero{height:578px;color:var(--white)}
.hero-bg{position:absolute;inset:0;background:linear-gradient(120deg,#3b2a52 0%,#a4475a 35%,#e07b4f 55%,#8f3b6a 75%,#2a1e45 100%)}
.nav{position:relative;display:flex;justify-content:space-between;align-items:center;padding:22px 72px}
.brand{font-size:22px;font-weight:500}
.menu{display:flex;gap:30px;list-style:none;font-size:15px}
.menu li+li::before{content:"•";margin-right:30px;opacity:.8}
.hero-body{position:relative;text-align:center;margin-top:118px}
.hero h1{font-size:44px;font-weight:500}
.hero .rule{background:var(--white)}
.hero p{width:820px;margin:0 auto 28px;font-size:13.5px;line-height:1.7;opacity:.9}
.hero .dots{position:absolute;left:0;right:0;top:543px}
.hero .dots i{background:rgba(255,255,255,.6)}
.hero .dots i.on{background:var(--white)}

/* about / integrations / donations */
.about{height:368px;padding-top:70px}
.about .tiles{margin-top:30px}
.integrations{height:361px;padding-top:60px}
.integrations .tiles{margin-top:30px}
.donations{height:371px;padding-top:62px}
.donations .tiles{margin-top:34px}

/* features grid */
.perks{height:408px;background:var(--red);color:var(--white)}
.perk{position:absolute;width:325px;height:147px;border:2px solid var(--white);padding:14px 18px 0 22px}
.perk::before{content:"";position:absolute;left:0;top:0;bottom:0;width:6px;background:var(--white)}
.perk h3{font-size:20px;font-weight:500;line-height:1.25;margin-bottom:8px}
.perk p{font-size:12.5px;line-height:1.65;opacity:.92}

/* platform */
.platform{height:334px;background:var(--dark);color:var(--white);padding-top:72px;text-align:center}
.platform-bg{position:absolute;inset:0;background:linear-gradient(135deg,#2a2a2a 0%,#363636 50%,#252525 100%)}
.platform>*:not(.platform-bg){position:relative}
.platform .rule{background:var(--white)}
.platform .copy{color:#ddd;margin-bottom:22px}
.platform .btn{border-color:var(--white)}

/* enterprise */
.enterprise{height:435px;background:var(--light)}
.enterprise-text{position:absolute;left:72px;top:60px;width:840px}
.enterprise-text h2{font-size:30px;font-weight:400}
.enterprise-text .rule{margin:10px 0 22px}
.enterprise-text p{font-size:13.5px;line-height:1.75;color:var(--muted);margin-bottom:18px}
.enterprise-art{position:absolute;left:868px;top:72px;width:262px;height:288px;background:linear-gradient(180deg,#6b6b6b,#3a3a3a)}

/* integrated solutions */
.solutions{height:424px;padding-top:46px}
.solutions-bg{position:absolute;inset:0;background:linear-gradient(180deg,#e9e3da 0%,#cfc8bf 55%,#b9b1a7 100%)}
.solutions>*:not(.solutions-bg){position:relative}
.solutions .tiles{gap:20px}
.solutions .tile{width:160px;height:106px;background:rgba(255,255,255,.55);border-color:#c8c2b9}
.solutions .tiles+.tiles{margin-top:22px}

/* plugins */
.plugins{height:278px;padding-top:40px}
.plugins .tiles{gap:26px}
.plugins .tile{width:152px}
.plugins .dots{margin-top:18px}

/* point of sale / billing */
.sales{height:465px;background:var(--purple);color:var(--white)}
.pos{position:absolute;left:72px;top:50px;width:420px}
.pos h2,.billing h2{font-size:28px;font-weight:400}
.pos ul{list-style:none;margin-top:20px}
.pos li{display:flex;align-items:center;gap:12px;font-size:13px;margin-bottom:12px}
.billing{position:absolute;left:524px;top:50px;width:610px}
.billing p{font-size:13px;line-height:1.7;margin:8px 0 24px;opacity:.9}
.billing .tiles{justify-content:flex-start;gap:24px;flex-wrap:wrap;width:560px}
.billing .tile{border:none}

/* code libraries */
.libraries{height:290px;background:var(--navy);color:var(--white);padding-top:50px}
.libraries .rule{background:var(--white)}
.libraries .tiles{gap:26px}
.libraries .tile{width:148px;height:104px;background:transparent;border-color:rgba(255,255,255,.35);color:var(--white)}
.libraries .dots{margin-top:16px}
.libraries .dots i{background:rgba(255,255,255,.4)}
.libraries .dots i.on{background:var(--white)}

/* pricing */
.pricing{height:629px;background:var(--light)}
.plan{position:absolute;background:var(--white);text-align:center;border:1px solid #e2e2e2}
.plan-head{height:70px;background:#3a3a3a;color:var(--white);font-size:20px;display:flex;align-items:center;justify-content:center}
.plan.featured .plan-head{background:var(--teal);height:86px}
.price{padding:22px 0 14px;border-bottom:1px solid #eee}
.price strong{font-size:44px;font-weight:500;line-height:1}
.price sup{font-size:16px;vertical-align:top;margin-right:4px}
.price small{display:block;font-size:12px;color:#888;margin-top:6px}
.plan ul{list-style:none}
.plan li{padding:13px 0;border-bottom:1px solid #eee;font-size:13.5px;color:var(--muted)}
.plan .btn{margin:28px 0 0;padding:8px 26px}
.plan.featured .btn{background:var(--teal);border-color:var(--teal)}

/* footer */
.footer{height:73px;background:var(--footer);color:#aaa;display:flex;align-items:center;justify-content:space-between;padding:0 72px;font-size:12.5px}
.social{display:flex;gap:10px}
.social i{width:26px;height:26px;border:1px solid #888;border-radius:50%}
.to-top{position:absolute;right:8px;bottom:8px;width:26px;height:26px;background:#3a3a3a}
</style>
</head>
<body>

<header class="hero">
  <div class="hero-bg" role="img" aria-label="Soft abstract background of warm orange and violet light"></div>
  <nav class="nav">
    <div class="brand">Micropayment Solutions</div>
    <ul class="menu"><li>Home</li><li>About Us</li><li>Services</li><li>News</li><li>Contact Us</li></ul>
  </nav>
  <div class="hero-body">
    <h1>Micropayment Solutions</h1>
    <div class="rule"></div>
    <p>Sed ut perspiciatis unde omnis iste natus error sit voluptatem accusantium doloremque laudantium, totam rem aperiam, eaque ipsa quae ab illo inventore veritatis et quasi architecto beatae vitae dicta sunt explicabo. Sed ut perspiciatis unde omnis iste natus.</p>
    <a class="btn">Learn More</a>
  </div>
  <div class="dots"><i class="on"></i><i></i></div>
</header>

<section class="about">
  <h2 class="title">About <b>Us</b></h2>
  <div class="rule"></div>
  <p class="copy">Sed ut perspiciatis unde omnis iste natus error sit voluptatem accusantium doloremque laudantium, totam rem aperiam, eaque ipsa quae ab illo inventore veritatis et quasi architecto beatae vitae dicta sunt explicabo Sed ut perspiciatis unde omnis iste natus error sit voluptatem accusantium doloremque laudantium, totam rem aperiam, eaque ipsa.</p>
  <div class="tiles">
    <div class="tile"><span class="dot" style="color:#e8901f"></span>Varnel</div>
    <div class="tile"><span class="dot" style="color:#9a9a9a"></span>Quorvath</div>
    <div class="tile"><span class="dot" style="color:#c9a441"></span>Fembrisk</div>
  </div>
</section>

<section class="perks">
  <div class="perk" style="left:84px;top:44px"><h3>Micropayments</h3><p>Doloremque laudantium, totam rem aperiam eaque ipsa quae ab illo inventore veritatis et quasi architecto beatae vitae.</p></div>
  <div class="perk" style="left:451px;top:44px"><h3>Save your money</h3><p>Doloremque laudantium, totam rem aperiam eaque ipsa quae ab illo inventore veritatis et quasi architecto beatae vitae.</p></div>
  <div class="perk" style="left:812px;top:44px"><h3>Sell your product to anyone, anywhere</h3><p>Doloremque laudantium, totam rem aperiam eaque ipsa quae ab illo inventore.</p></div>
  <div class="perk" style="left:261px;top:217px"><h3>End chargeback fraud an identity theft</h3><p>Doloremque laudantium, totam rem aperiam eaque ipsa quae ab illo inventore.</p></div>
  <div class="perk" style="left:618px;top:217px"><h3>Exchange rates</h3><p>Doloremque laudantium, totam rem aperiam eaque ipsa quae ab illo inventore veritatis et quasi architecto beatae vitae.</p></div>
</section>

<section class="platform">
  <div class="platform-bg" role="img" aria-label="Dark faceted geometric background"></div>
  <h2 class="title">Features Platform</h2>
  <div class="rule"></div>
  <p class="copy">Sed ut perspiciatis unde omnis iste natus error sit voluptatem accusantium doloremque laudantium, totam rem aperiam, eaque ipsa quae ab illo inventore veritatis et quasi architecto beatae vitae dicta sunt explicabo Sed ut perspiciatis unde omnis iste natus Sed ut perspiciatis unde omnis iste natus error sit voluptatem accusantium doloremque laudantium, totam rem.</p>
  <a class="btn btn-solid">Learn More</a>
</section>

<section class="enterprise">
  <div class="enterprise-text">
    <h2>Enterprices</h2>
    <div class="rule"></div>
    <p>Sed ut perspiciatis unde omnis iste natus error sit voluptatem accusantium doloremque laudantium, totam rem aperiam, eaque ipsa quae ab illo inventore veritatis et quasi architecto beatae vitae dicta sunt explicabo Sed ut perspiciatis unde omnis iste natus Sed ut perspiciatis unde omnis iste natus error sit voluptatem accusantium doloremque laudantium, totam rem.</p>
    <p>Quasi architecto beatae vitae dicta sunt explicabo Sed ut perspiciatis unde omnis iste natus Sed ut perspiciatis unde omnis iste natus error sit voluptatem accusantium doloremque laudantium, totam rem.</p>
    <a class="btn btn-dark">Learn More</a>
  </div>
  <div class="enterprise-art" role="img" aria-label="Illustration of an office tower with an enterprise banner"></div>
</section>

<section class="integrations">
  <h2 class="title">Integrations</h2>
  <div class="rule"></div>
  <p class="copy">Sed ut perspiciatis unde omnis iste natus error sit voluptatem accusantium doloremque laudantium, totam rem aperiam, eaque ipsa quae ab illo inventore veritatis et quasi architecto beatae vitae dicta sunt explicabo Sed ut perspiciatis unde omnis iste natus error sit voluptatem accusantium doloremque laudantium, totam rem aperiam, eaque ipsa.</p>
  <div class="tiles">
    <div class="tile"><span class="dot" style="color:#e8901f"></span>Varnel</div>
    <div class="tile"><span class="dot" style="color:#9a9a9a"></span>Quorvath</div>
    <div class="tile"><span class="dot" style="color:#c9a441"></span>Fembrisk</div>
  </div>
</section>

<section class="solutions">
  <div class="solutions-bg" role="img" aria-label="Faded photograph of a city skyline"></div>
  <h2 class="title">Integrated Solutions</h2>
  <div class="rule"></div>
  <div class="tiles">
    <div class="tile" style="color:#3f8a2a">Tessavo</div>
    <div class="tile" style="color:#3f8a2a">Powerly</div>
    <div class="tile" style="color:#5c8f3a">Markloom</div>
    <div class="tile">Triden</div>
    <div class="tile" style="color:#4d8a3a">Botrix</div>
    <div class="tile" style="color:#2f4d80">Ventrix</div>
  </div>
  <div class="tiles">
    <div class="tile" style="color:#c8282e">Baskely</div>
    <div class="tile" style="color:#2f3d7a">Swiftor</div>
    <div class="tile" style="color:#4d8a3a">Trolley</div>
    <div class="tile" style="color:#c8282e">Zephro</div>
    <div class="tile" style="color:#2f5d8a">Civora</div>
  </div>
</section>

<section class="plugins">
  <h2 class="title">Opensource plugins</h2>
  <div class="rule"></div>
  <div class="tiles">
    <div class="tile" style="color:#e2642b">Plindor</div>
    <div class="tile" style="color:#2f7ac8">Shelvio</div>
    <div class="tile" style="color:#5a6a6a">Cubix</div>
    <div class="tile" style="color:#3a8a7a">Tradlo</div>
    <div class="tile" style="color:#2fa5d8">Cartwell</div>
    <div class="tile" style="color:#3a4a9a">Orbella</div>
  </div>
  <div class="dots"><i class="on"></i><i></i></div>
</section>

<section class="sales">
  <div class="pos">
    <h2>Point of sale</h2>
    <ul>
      <li><svg width="16" height="16" viewBox="0 0 16 16"><circle cx="8" cy="8" r="7" fill="none" stroke="#fff" stroke-width="1.4"/><path d="M4.5 8.2l2.3 2.3 4.7-4.8" fill="none" stroke="#fff" stroke-width="1.6"/></svg>Sed ut perspiciatis unde omnis iste natus</li>
      <li><svg width="16" height="16" viewBox="0 0 16 16"><circle cx="8" cy="8" r="7" fill="none" stroke="#fff" stroke-width="1.4"/><path d="M4.5 8.2l2.3 2.3 4.7-4.8" fill="none" stroke="#fff" stroke-width="1.6"/></svg>error sit voluptatem accusantium doloremque</li>
      <li><svg width="16" height="16" viewBox="0 0 16 16"><circle cx="8" cy="8" r="7" fill="none" stroke="#fff" stroke-width="1.4"/><path d="M4.5 8.2l2.3 2.3 4.7-4.8" fill="none" stroke="#fff" stroke-width="1.6"/></svg>laudantium, totam rem aperiam, eaque</li>
      <li><svg width="16" height="16" viewBox="0 0 16 16"><circle cx="8" cy="8" r="7" fill="none" stroke="#fff" stroke-width="1.4"/><path d="M4.5 8.2l2.3 2.3 4.7-4.8" fill="none" stroke="#fff" stroke-width="1.6"/></svg>ipsa quae ab illo inventore veritatis et quasi</li>
      <li><svg width="16" height="16" viewBox="0 0 16 16"><circle cx="8" cy="8" r="7" fill="none" stroke="#fff" stroke-width="1.4"/><path d="M4.5 8.2l2.3 2.3 4.7-4.8" fill="none" stroke="#fff" stroke-width="1.6"/></svg>architecto beatae vitae dicta sunt explicabo.</li>
      <li><svg width="16" height="16" viewBox="0 0 16 16"><circle cx="8" cy="8" r="7" fill="none" stroke="#fff" stroke-width="1.4"/><path d="M4.5 8.2l2.3 2.3 4.7-4.8" fill="none" stroke="#fff" stroke-width="1.6"/></svg>ut perspiciatis unde omnis iste natus</li>
    </ul>
  </div>
  <div class="billing">
    <h2>Billinig and Accounting</h2>
    <p>Sed ut perspiciatis unde omnis iste natus Sed ut perspiciatis unde omnis iste natus error sit voluptatem accusantium doloremque laudantium, totam rem aperiam, eaque ipsa quae ab illo.</p>
    <div class="tiles">
      <div class="tile" style="color:#2f3d5a">Billmora</div>
      <div class="tile" style="color:#3a9a3a">Ledgrin</div>
      <div class="tile" style="color:#2fa5c8">Payvue</div>
      <div class="tile" style="color:#2f3d5a">Numbry</div>
      <div class="tile" style="color:#6aa52f">Gearix</div>
    </div>
  </div>
</section>

<section class="donations">
  <h2 class="title">Donations</h2>
  <div class="rule"></div>
  <p class="copy">Sed ut perspiciatis unde omnis iste natus error sit voluptatem accusantium doloremque laudantium, totam rem aperiam, eaque ipsa quae ab illo inventore veritatis et quasi architecto beatae vitae dicta sunt explicabo Sed ut perspiciatis unde omnis iste natus Sed ut perspiciatis unde omnis iste natus error sit voluptatem accusantium doloremque laudantium, totam rem aperiam, eaque ipsa.</p>
  <div class="tiles">
    <div class="tile" style="color:#d8b21f">Giveta</div>
    <div class="tile" style="color:#2f8ac8">Towerly</div>
    <div class="tile" style="color:#2f6ac8">Kindra</div>
    <div class="tile" style="color:#2f5da8">Globana</div>
  </div>
</section>

<section class="libraries">
  <h2 class="title">Code libraries</h2>
  <div class="rule"></div>
  <div class="tiles">
    <div class="tile">Droven</div>
    <div class="tile">Kitlo</div>
    <div class="tile">Orchal</div>
    <div class="tile">Nodara</div>
    <div class="tile">Serpix</div>
    <div class="tile">Dropla</div>
  </div>
  <div class="dots"><i class="on"></i><i></i></div>
</section>

<section class="pricing">
  <div class="plan" style="left:90px;top:107px;width:321px;height:445px">
    <div class="plan-head">Package 1</div>
    <div class="price"><sup>$</sup><strong>9.99</strong><small>per month</small></div>
    <ul><li>Feature One</li><li>Feature Two</li><li>Feature Three</li></ul>
    <a class="btn btn-dark">Learn More</a>
  </div>
  <div class="plan featured" style="left:438px;top:87px;width:321px;height:470px">
    <div class="plan-head">Package 2</div>
    <div class="price"><sup>$</sup><strong>19.99</strong><small>per month</small></div>
    <ul><li>Feature One</li><li>Feature Two</li><li>Feature Three</li></ul>
    <a class="btn btn-dark">Learn More</a>
  </div>
  <div class="plan" style="left:792px;top:107px;width:318px;height:445px">
    <div class="plan-head">Package 3</div>
    <div class="price"><sup>$</sup><strong>59.99</strong><small>per year</small></div>
    <ul><li>Feature One</li><li>Feature Two</li><li>Feature Three</li></ul>
    <a class="btn btn-dark">Learn More</a>
  </div>
</section>

<footer class="footer">
  <span>Copyright © 2015 Yourcitename All rights reserved.</span>
  <div class="social"><i></i><i></i><i></i><i></i></div>
  <div class="to-top"></div>
</footer>

</body>
</html>
```